Events By Quellon

Weddings, Corporate, Special Events
Memorable Catering, Personalized Menus, Custom Layout & Designs
Professional Staff, Excellent Service
Our Mission is Turning YOUR Vision into a Reality

Dorrie Quellon, Principal Planner
ph. 202 555-0187 - fax 301-555-0142
Email - eventsbyquellon@mailhaven.net
Web - www.cateringbyquellon.net
cateringbyquellon@Instagram

Target Market(s)

All Brides, Corprate Business, Special Events

Industry/Entity Type

Hospitality

Contact Information for Business Card

clean but affective

Font styles to use
Serif
Sans Serif
Script

Colors

Designer to choose colors to be used in the design.

Requirements
Must have
• logo with tagline using colors that will enhance what
• some pictures of nice table scape, hors d'oevures, upscale foods......
Nice to have
• Event: Something that happens or is regarded as happening, an occurrence especially one of some importance.
Should not have
• Use Logo on both sides

```html
<!DOCTYPE html>
<html lang="en">
<head>
<meta charset="utf-8">
<title>Events By Quellon – Business Card</title>
<link rel="stylesheet" href="https://fonts.googleapis.com/css2?family=Cinzel:wght@400;600&family=Open+Sans:wght@400&display=swap">
<style>
  :root {
    --backdrop: #e4e4e2;
    --card: #141719;
    --teal: #1a9ea8;
    --teal-deep: #137781;
    --grey: #7e8487;
    --edge: #0f6f78;
  }
  * { box-sizing: border-box; margin: 0; padding: 0; }
  html, body { width: 1200px; height: 1021px; overflow: hidden; }
  body {
    background: var(--backdrop);
    display: flex;
    flex-direction: column;
    align-items: center;
    justify-content: center;
    gap: 48px;
  }
  .card {
    width: 760px;
    height: 434px;
    background: var(--card);
    border-bottom: 6px solid var(--edge);
    border-radius: 4px;
    position: relative;
    box-shadow: 0 10px 24px rgba(0,0,0,.25);
  }
  .brand {
    display: flex;
    flex-direction: column;
    align-items: center;
    color: var(--teal);
    font-family: "Cinzel", serif;
  }
  .brand-mark {
    width: 64px; height: 64px;
    border: 3px solid var(--grey);
    border-radius: 50%;
    margin-bottom: 14px;
  }
  .brand-name { font-size: 34px; font-weight: 600; letter-spacing: 1px; }
  .brand-tagline { font-size: 11px; letter-spacing: 1px; margin-top: 4px; color: var(--teal-deep); }

  .card-front { display: flex; flex-direction: column; align-items: center; justify-content: center; }
  .mission {
    margin-top: 38px;
    font-family: "Cinzel", serif;
    font-size: 15px;
    letter-spacing: 1px;
    color: var(--teal-deep);
  }

  .card-back { display: flex; align-items: center; padding: 0 56px; }
  .card-back .brand { width: 330px; margin-top: 80px; }
  .card-back .brand-name { font-size: 28px; }
  .card-back .brand-mark { width: 56px; height: 56px; }
  .contact { margin-left: 34px; margin-bottom: 40px; }
  .contact-name { font-family: "Cinzel", serif; font-size: 24px; color: var(--grey); letter-spacing: 1px; }
  .contact-role { font-family: "Cinzel", serif; font-size: 16px; color: var(--teal-deep); letter-spacing: 1px; margin-bottom: 14px; }
  .contact-list { list-style: none; font-family: "Open Sans", sans-serif; font-size: 14px; color: var(--grey); }
  .contact-list li { display: flex; align-items: center; gap: 12px; line-height: 24px; }
  .contact-list svg { width: 14px; height: 14px; fill: none; stroke: var(--grey); stroke-width: 1.6; flex: none; }
</style>
</head>
<body>
  <section class="card card-front">
    <div class="brand">
      <span class="brand-mark"></span>
      <span class="brand-name">Events By Quellon</span>
      <span class="brand-tagline">Events Designed with You in mind</span>
    </div>
    <p class="mission">Our Mission is Turning YOUR Vision into a Reality</p>
  </section>

  <section class="card card-back">
    <div class="brand">
      <span class="brand-mark"></span>
      <span class="brand-name">Events By Quellon</span>
      <span class="brand-tagline">Events Designed with You in mind</span>
    </div>
    <div class="contact">
      <p class="contact-name">Dorrie Quellon</p>
      <p class="contact-role">Principal Planner</p>
      <ul class="contact-list">
        <li><svg viewBox="0 0 14 14"><path d="M3 1l2 3-1.5 1.5a8 8 0 0 0 5 5L10 9l3 2-1 2C6 13 1 8 1 2z"/></svg>202 555-0187</li>
        <li><svg viewBox="0 0 14 14"><rect x="1" y="5" width="12" height="7"/><rect x="4" y="1" width="6" height="4"/></svg>301-555-0142</li>
        <li><svg viewBox="0 0 14 14"><rect x="1" y="3" width="12" height="8"/><path d="M1 3l6 5 6-5"/></svg>www.cateringbyquellon.net</li>
        <li><svg viewBox="0 0 14 14"><circle cx="7" cy="7" r="6"/><path d="M1 7h12M7 1c-3 3-3 9 0 12M7 1c3 3 3 9 0 12"/></svg>eventsbyquellon@mailhaven.net</li>
        <li><svg viewBox="0 0 14 14"><rect x="1.5" y="1.5" width="11" height="11"/></svg>cateringbyquellon@Instagram</li>
      </ul>
    </div>
  </section>
</body>
</html>
```